Cosmetics Brand Logo and Bottle Label Design

We are creating a new cosmetics brand called "Nolan Whitby" and would like you to create an amazing logo and bottle label for this brand's new 100% pure argan oil product.
For the logo, we really like the logo's of Marin Calloway and Vessa. The text should be Sans Serif (without feet).
For the actual bottle label, please find attached labels of one of our competitors design which really like. We really like the simplicity and elegance of the design. The only difference is that our product will be using light turqoise as the brand color. Please feel free to add your own creativity into it as well.
Industry/Entity Type
Cosmetics
Logo Text
Nolan Whitby
Font styles to use

```html
<!DOCTYPE html>
<html lang="en">
<head>
<meta charset="utf-8">
<title>Nolan Whitby – 100% Pure Argan Oil Label</title>
<link rel="stylesheet" href="https://fonts.googleapis.com/css2?family=Cabin:wght@400&display=swap">
<style>
  :root {
    --stage: #e4e6e9;
    --label: #f7f8f8;
    --brand-teal: #3fb5a5;
    --soft-teal: #7fcfc4;
    --tree-teal: #a9ddd7;
    --tree-light: #cdece8;
    --fine-grey: #8a8f93;
  }
  html, body {
    margin: 0;
    width: 1200px;
    height: 1200px;
    overflow: hidden;
    background: var(--stage);
  }
  .canvas {
    position: relative;
    width: 1200px;
    height: 1200px;
    display: flex;
    align-items: center;
    justify-content: center;
  }
  .label {
    position: relative;
    width: 420px;
    height: 1150px;
    background: var(--label);
    box-shadow: 0 2px 10px rgba(0,0,0,0.08);
    overflow: hidden;
    font-family: "Cabin", "Candara", sans-serif;
    text-align: center;
  }
  .brand-name {
    position: absolute;
    top: 142px;
    left: 22px;
    right: 22px;
    margin: 0;
    padding-bottom: 6px;
    border-bottom: 2px solid var(--brand-teal);
    color: var(--brand-teal);
    font-size: 42px;
    font-weight: 400;
    letter-spacing: 1px;
    text-transform: uppercase;
    line-height: 1;
  }
  .purity {
    position: absolute;
    top: 286px;
    left: 0;
    right: 0;
    margin: 0;
    color: var(--soft-teal);
    font-size: 32px;
    font-weight: 400;
    line-height: 1;
  }
  .product-name {
    position: absolute;
    top: 318px;
    left: 0;
    right: 0;
    margin: 0;
    color: var(--soft-teal);
    font-size: 88px;
    font-weight: 400;
    line-height: 1;
  }
  .volume {
    position: absolute;
    top: 478px;
    left: 0;
    right: 0;
    margin: 0;
    color: var(--fine-grey);
    font-size: 22px;
    font-weight: 400;
    line-height: 1;
  }
  .tree-artwork {
    position: absolute;
    left: 0;
    bottom: 0;
    width: 420px;
    height: 610px;
    display: block;
  }
</style>
</head>
<body>
  <main class="canvas">
    <section class="label">
      <h1 class="brand-name">Nolan Whitby</h1>
      <p class="purity">100% Pure</p>
      <h2 class="product-name">Argan Oil</h2>
      <p class="volume">120 mL 4fl. oz.</p>
      <svg class="tree-artwork" viewBox="0 0 420 610" preserveAspectRatio="none" role="img" aria-label="Illustration of a leafy argan tree with fruit in light turquoise, filling the lower half of the label">
        <defs>
          <linearGradient id="treeFade" x1="0" y1="0" x2="0" y2="1">
            <stop offset="0%" stop-color="#cdece8" stop-opacity="0"/>
            <stop offset="12%" stop-color="#cdece8" stop-opacity="0.7"/>
            <stop offset="35%" stop-color="#bfe6e1"/>
            <stop offset="100%" stop-color="#b2e0da"/>
          </linearGradient>
        </defs>
        <rect x="0" y="0" width="420" height="610" fill="url(#treeFade)"/>
      </svg>
    </section>
  </main>
</body>
</html>
```